" Empresa que trabalha com danças urbanas. Workhops, Batalhas, Performances, Palestras, Bate-papos, Jam Sessions. Também possui um projeto social em comunidades. "

```html
<!DOCTYPE html>
<html lang="pt-BR">
<head>
<meta charset="utf-8">
<title>Ritmo Urbano — Danças Urbanas</title>
<link rel="stylesheet" href="https://fonts.googleapis.com/css2?family=Oswald:wght@400;600;700&family=Open+Sans:wght@400;600&display=swap">
<style>
  :root{
    --canvas:#ffffff;
    --page:#262626;
    --page-dark:#1b1b1b;
    --panel:#333333;
    --silver-light:#f2f2f2;
    --silver:#bfbfbf;
    --silver-dark:#8a8a8a;
    --green:#4cae1f;
    --green-dark:#2f7d12;
    --text:#d8d8d8;
    --text-dim:#9a9a9a;
    --white:#ffffff;
    --photo-crowd:#5a6272;
    --photo-floor:#8c8c8c;
    --photo-stage:#c0622a;
    --photo-night:#3a2e2a;
  }
  *{box-sizing:border-box;margin:0;padding:0}
  html,body{width:1200px;height:1200px;overflow:hidden;background:var(--canvas)}
  body{position:relative;font-family:"Open Sans",Arial,sans-serif;color:var(--text)}
  .page{position:absolute;left:336px;top:0;width:528px;height:1200px;
    background:linear-gradient(180deg,var(--page) 0%,var(--page-dark) 100%)}
  .abs{position:absolute}

  /* header */
  .topbar{left:0;top:0;width:528px;height:34px;background:#141414}
  .member-box{left:30px;top:10px;width:50px;height:16px;border:1px solid var(--silver-dark);
    font-size:5px;line-height:14px;text-align:center;color:var(--text-dim)}
  .social-top{right:14px;top:13px;display:flex;gap:3px}
  .dot{width:9px;height:9px;border-radius:50%;background:var(--silver)}
  .header-band{left:0;top:34px;width:528px;height:76px;
    background:linear-gradient(180deg,var(--silver-light),var(--silver) 60%,var(--silver-dark))}
  .header-curve{left:0;top:34px}
  .brand{left:176px;top:14px;width:176px;height:86px;border-radius:6px;
    background:linear-gradient(180deg,#3a3a3a,#161616);border:2px solid var(--silver);
    display:flex;flex-direction:column;align-items:center;justify-content:center}
  .brand-name{font-family:"Oswald",sans-serif;font-weight:700;font-size:28px;color:var(--white);letter-spacing:1px;line-height:1}
  .brand-tag{font-family:"Oswald",sans-serif;font-weight:700;font-size:28px;color:var(--white);line-height:1}
  .dancer{left:462px;top:40px;width:44px;height:58px;border-radius:4px;
    background:linear-gradient(180deg,#5d5d5d,#2e2e2e)}
  .nav{left:0;top:110px;width:528px;height:16px;background:#111;
    display:flex;justify-content:center;gap:11px;align-items:center}
  .nav a{font-family:"Oswald",sans-serif;font-size:6.5px;color:var(--white);text-decoration:none;letter-spacing:.4px}
  .subnav{left:0;top:131px;width:528px;height:12px;border-top:1px solid var(--green-dark);border-bottom:1px solid var(--green-dark);
    display:flex;justify-content:center;gap:14px;align-items:center}
  .subnav a{font-size:5.5px;color:var(--green);text-decoration:none}

  /* slider */
  .slider{left:29px;top:158px;width:470px;height:154px;
    background:linear-gradient(180deg,var(--photo-crowd) 0%,#6b5e58 55%,var(--photo-floor) 100%);
    border:1px solid #444}
  .slider-dots{left:0;top:321px;width:528px;display:flex;justify-content:center;gap:4px}
  .slider-dots span{width:4px;height:4px;border-radius:50%;background:var(--silver-dark)}
  .slider-dots span:first-child{background:var(--white)}

  /* intro */
  .intro{left:29px;top:353px;width:470px;height:127px;border:3px solid var(--silver-dark);background:var(--panel)}
  .portrait{left:16px;top:8px;width:96px;height:84px;background:linear-gradient(180deg,#7d7d7d,#2c2c2c)}
  .person{left:16px;top:96px;display:flex;align-items:center;gap:5px;font-family:"Oswald",sans-serif;font-size:10px;color:var(--white)}
  .person .mark{width:10px;height:10px;border-radius:50%;background:var(--green)}
  .intro-title{left:150px;top:12px;width:300px;text-align:center;font-family:"Oswald",sans-serif;font-size:13px;color:var(--white);letter-spacing:.5px}
  .intro-text{left:150px;top:34px;width:300px;font-size:6.5px;line-height:10px;color:var(--text)}
  .intro-role{left:150px;top:100px;width:300px;text-align:center;font-family:"Oswald",sans-serif;font-size:6.5px;color:var(--white)}

  /* cards */
  .card{width:180px;height:160px}
  .card-tab{left:10px;top:0;width:160px;height:22px;border-radius:3px 3px 0 0;
    background:linear-gradient(180deg,var(--silver-light),var(--silver-dark));
    font-family:"Oswald",sans-serif;font-weight:600;font-size:10px;color:#222;text-align:center;line-height:22px}
  .card-photo{left:0;top:22px;width:180px;height:76px;border:2px solid #111;
    background:radial-gradient(ellipse at 50% 70%,#f3a45a 0%,var(--photo-stage) 35%,var(--photo-night) 80%)}
  .card-text{left:0;top:104px;width:180px;font-size:5.8px;line-height:9px;color:var(--text)}

  /* video */
  .video{left:77px;top:852px;width:380px;height:108px;border:2px solid #111;
    background:linear-gradient(180deg,#4b4b55 0%,#6e6a66 50%,#9a9a9a 100%)}

  /* thumbs */
  .thumb{top:989px;width:84px;height:96px;background:#1e1e1e;border:2px solid var(--silver-dark)}
  .thumb-photo{left:4px;top:4px;width:72px;height:66px;background:linear-gradient(180deg,#9a9a9a,#4a4a4a)}
  .thumb-label{left:0;top:74px;width:80px;text-align:center;font-family:"Oswald",sans-serif;font-size:7px;color:var(--white)}
  .to-top{left:503px;top:1072px;width:14px;height:14px;background:#ddd;border-radius:2px}

  /* footer */
  .social-foot{left:0;top:1102px;width:528px;display:flex;justify-content:center;gap:3px}
  .footer-band{left:0;top:1116px;width:528px;height:42px;
    background:linear-gradient(180deg,var(--silver-dark),var(--silver-light) 50%,var(--silver-dark))}
  .footer-brand{left:224px;top:1121px;width:80px;height:32px;background:#1a1a1a;border:1px solid var(--silver);
    font-family:"Oswald",sans-serif;font-weight:700;font-size:11px;color:var(--white);text-align:center;line-height:30px}
  .copyright{left:0;top:1172px;width:528px;text-align:center;font-size:5.5px;color:var(--text-dim)}
</style>
</head>
<body>
<div class="page">
  <header>
    <div class="abs topbar"></div>
    <div class="abs member-box">Área do aluno</div>
    <div class="abs social-top"><span class="dot"></span><span class="dot"></span><span class="dot"></span><span class="dot"></span><span class="dot"></span></div>
    <div class="abs header-band"></div>
    <svg class="abs header-curve" width="528" height="76" viewBox="0 0 528 76">
      <path d="M0 60 Q264 30 528 52 L528 76 L0 76 Z" fill="#6e6e6e" opacity=".55"/>
      <path d="M0 66 Q264 40 528 60" stroke="#ffffff" stroke-width="1.5" fill="none" opacity=".7"/>
    </svg>
    <div class="abs brand">
      <span class="brand-name">RITMO</span>
      <span class="brand-tag">URBANO</span>
    </div>
    <div class="abs dancer" role="img" aria-label="Silhueta de dançarino em movimento"></div>
    <nav class="abs nav">
      <a>HOME</a><a>SOBRE</a><a>SERVIÇOS</a><a>PROJETO SOCIAL</a><a>PARCEIROS</a><a>AGENDA</a><a>VÍDEOS</a><a>FOTOS</a><a>CONTATO</a>
    </nav>
    <div class="abs subnav"><a>Workshops</a><a>Batalhas</a><a>Performances</a><a>Palestras</a></div>
  </header>

  <section>
    <div class="abs slider" role="img" aria-label="Foto de dançarino fazendo breaking em uma roda com público ao redor"></div>
    <div class="abs slider-dots"><span></span><span></span><span></span><span></span><span></span></div>
  </section>

  <section class="abs intro">
    <div class="abs portrait" role="img" aria-label="Retrato do diretor de boné"></div>
    <div class="abs person"><span class="mark"></span>Rafael Nunes</div>
    <h2 class="abs intro-title">RITMO URBANO</h2>
    <p class="abs intro-text">Somos um coletivo de danças urbanas que leva workshops, batalhas, performances, palestras e bate-papos a todo o país, com um projeto social em comunidades.<br><br>Conheça a equipe e acompanhe a agenda.</p>
    <p class="abs intro-role">DIRETOR NACIONAL</p>
  </section>

  <section>
    <article class="abs card" style="left:72px;top:511px">
      <div class="abs card-tab">BATALHA URBANA</div>
      <div class="abs card-photo" role="img" aria-label="Foto de batalha de dança sob luzes de palco"></div>
      <p class="abs card-text">Confira a próxima batalha urbana com dançarinos de várias cidades, jurados convidados e muita música na roda.</p>
    </article>
    <article class="abs card" style="left:276px;top:511px">
      <div class="abs card-tab">BATALHA URBANA</div>
      <div class="abs card-photo" role="img" aria-label="Foto de batalha de dança sob luzes de palco"></div>
      <p class="abs card-text">Confira a próxima batalha urbana com dançarinos de várias cidades, jurados convidados e muita música na roda.</p>
    </article>
    <article class="abs card" style="left:72px;top:679px">
      <div class="abs card-tab">BATALHA URBANA</div>
      <div class="abs card-photo" role="img" aria-label="Foto de batalha de dança sob luzes de palco"></div>
      <p class="abs card-text">Confira a próxima batalha urbana com dançarinos de várias cidades, jurados convidados e muita música na roda.</p>
    </article>
    <article class="abs card" style="left:276px;top:679px">
      <div class="abs card-tab">BATALHA URBANA</div>
      <div class="abs card-photo" role="img" aria-label="Foto de batalha de dança sob luzes de palco"></div>
      <p class="abs card-text">Confira a próxima batalha urbana com dançarinos de várias cidades, jurados convidados e muita música na roda.</p>
    </article>
  </section>

  <section>
    <div class="abs video" role="img" aria-label="Vídeo de roda de dança em piso quadriculado com plateia"></div>
  </section>

  <section>
    <div class="abs thumb" style="left:68px"><div class="abs thumb-photo" role="img" aria-label="Foto de batalha"></div><span class="abs thumb-label">BATALHAS</span></div>
    <div class="abs thumb" style="left:168px"><div class="abs thumb-photo" role="img" aria-label="Foto de workshop"></div><span class="abs thumb-label">WORKSHOPS</span></div>
    <div class="abs thumb" style="left:271px"><div class="abs thumb-photo" role="img" aria-label="Foto do projeto social"></div><span class="abs thumb-label">SOCIAL</span></div>
    <div class="abs thumb" style="left:374px"><div class="abs thumb-photo" role="img" aria-label="Foto de notícias"></div><span class="abs thumb-label">NEWS</span></div>
    <svg class="abs to-top" viewBox="0 0 14 14"><path d="M3 9 L7 5 L11 9" stroke="#222" stroke-width="2" fill="none"/></svg>
  </section>

  <footer>
    <div class="abs social-foot"><span class="dot"></span><span class="dot"></span><span class="dot"></span><span class="dot"></span><span class="dot"></span></div>
    <div class="abs footer-band"></div>
    <div class="abs footer-brand">RITMO URBANO</div>
    <p class="abs copyright">© 2024 Ritmo Urbano · Todos os direitos reservados</p>
  </footer>
</div>
</body>
</html>
```